Simple and clean webdesign for personal homepage

Trying to create a simple and clean webdesign for my personal homepage. Going to use a static site builder with templates to build the site. I want it to have multiple pages - like an about me, blog and resume. I just need something very basic I can customize. I want the main colors to be purple, black and white. I am open to other color palettes too but since purple is my favorite color I want that to be one of the main colors.

The site be mostly text driven. Might have some images in the body text but I want the site design to be light and lean.

Industry/Entity Type

Personal Homepage.

Coding

Coded - Design and coding required

Number of Pages Required

1 page

Font styles to use
Sans Serif

Colors
6B429C
8869AF
B7A5CE
E3DAEB
F3F0F8

Requirements
Must have
• Clean design. Purple used as a color. HTML template.
Nice to have
• Responsive

```html
<!DOCTYPE html>
<html lang="en">
<head>
<meta charset="UTF-8">
<title>Personal Homepage</title>
<link href="https://fonts.googleapis.com/css2?family=Playfair+Display:wght@400;700&family=Roboto:wght@400;500&display=swap" rel="stylesheet">
<style>
:root{
  --purple-deep:#6B429C;
  --purple:#8869AF;
  --purple-soft:#B7A5CE;
  --lilac:#E3DAEB;
  --mist:#F3F0F8;
  --ink:#1d1a22;
  --text:#3a3640;
  --muted:#6d6875;
  --white:#ffffff;
}
*{box-sizing:border-box;margin:0;padding:0}
html,body{width:1200px;height:4376px;overflow:hidden}
body{font-family:'Roboto',sans-serif;color:var(--text);background:var(--white)}
.serif{font-family:'Playfair Display',serif}
h1,h2,h3,.logo,.main-nav a,.btn,.footer-nav a{font-family:'Playfair Display',serif}

/* Hero */
.hero{position:relative;height:640px;color:var(--white);text-align:center;overflow:hidden}
.hero-photo{position:absolute;inset:0;background:
  linear-gradient(180deg,#7b5fb8 0%,#9a7dd0 22%,#c392d6 40%,#a37bc9 55%,#5c3f8d 72%,#7a5fa8 86%,#b7a5ce 100%)}
.hero-inner{position:relative}
.site-header{display:flex;justify-content:space-between;align-items:center;padding:44px 168px 0}
.logo{font-size:30px;font-weight:700;letter-spacing:1px}
.main-nav{display:flex;gap:26px}
.main-nav a{color:var(--white);text-decoration:none;font-size:19px}
.hero h1{margin-top:130px;font-size:46px;font-weight:700}
.hero-lead{width:640px;margin:16px auto 0;font-size:16px;line-height:1.55;opacity:.95}
.btn{display:inline-block;text-transform:uppercase;font-weight:700;text-decoration:none;letter-spacing:.5px}
.btn-outline{margin-top:30px;width:228px;height:62px;line-height:58px;border:2px solid var(--white);border-radius:31px;color:var(--white);font-size:18px;background:rgba(107,66,156,.35)}
.btn-solid{width:290px;height:72px;line-height:72px;border-radius:36px;background:var(--purple-deep);color:var(--white);font-size:15px}

/* Sections */
.section-title{font-size:46px;font-weight:700;color:var(--purple-deep);text-transform:uppercase;text-align:center}
.about{height:600px;padding-top:110px;text-align:center}
.about p{width:860px;margin:32px auto 40px;font-size:17px;line-height:1.5;color:var(--ink)}

.mail{position:relative;height:368px;text-align:center;color:var(--white);overflow:hidden}
.mail-photo{position:absolute;inset:0;background:linear-gradient(180deg,#a894c6 0%,#b9a8d2 45%,#c5b7db 70%,#b3a0cc 100%)}
.mail-inner{position:relative;padding-top:68px}
.mail h2{font-size:46px;font-weight:700;text-transform:uppercase;letter-spacing:1px}
.mail p{width:640px;margin:18px auto 0;font-size:16px;line-height:1.45}
.signup{display:flex;justify-content:center;margin-top:46px}
.signup-field{width:448px;height:54px;background:var(--white);border-radius:27px 0 0 27px;padding-left:28px;display:flex;align-items:center;color:#9d98a5;font-size:13px;text-transform:uppercase}
.signup-btn{width:180px;height:54px;background:var(--purple);border-radius:0 27px 27px 0;display:flex;align-items:center;justify-content:center;font-family:'Playfair Display',serif;font-size:14px;text-transform:uppercase;letter-spacing:.5px}

.courses{height:840px;padding-top:110px;text-align:center}
.course-grid{display:grid;grid-template-columns:repeat(2,440px);column-gap:20px;row-gap:70px;justify-content:center;margin:60px 0 60px;text-align:left}
.course{display:flex;gap:26px}
.course-icon{flex:0 0 72px;height:72px;border-radius:50%;background:var(--purple-deep);display:flex;align-items:center;justify-content:center}
.course h3{font-size:20px;font-weight:700;line-height:1.25;color:var(--ink)}
.course p{margin-top:10px;font-size:16px;line-height:1.35;color:var(--ink)}

/* Blog */
.blog{position:relative;height:1552px;padding-top:58px;overflow:hidden}
.blog-photo{position:absolute;inset:0;background:linear-gradient(180deg,#d6cbe6 0%,#e3daeb 35%,#d8cde8 65%,#c9badf 100%)}
.blog-inner{position:relative}
.blog-grid{display:flex;gap:20px;width:856px;margin:58px auto 0}
.blog-col{flex:1;display:flex;flex-direction:column;gap:22px}
.post{background:var(--white);padding:26px 22px 24px;box-shadow:0 2px 8px rgba(107,66,156,.12)}
.post h3{font-size:17px;font-weight:700;line-height:1.3;color:var(--ink)}
.post p{margin-top:16px;font-size:13px;line-height:1.5;color:var(--muted)}
.post-date{display:flex;align-items:center;gap:8px;margin-top:18px;font-size:13px;color:var(--ink)}
.pager{display:flex;justify-content:center;gap:12px;margin-top:40px}
.pager span{width:44px;height:44px;border-radius:50%;border:1.5px solid var(--white);display:flex;align-items:center;justify-content:center;color:var(--white);font-size:13px;background:rgba(136,105,175,.45)}
.pager .active{background:var(--purple-deep);border-color:var(--purple-deep)}

/* Footer */
.site-footer{position:relative;height:376px;color:var(--white);text-align:center;overflow:hidden}
.footer-photo{position:absolute;inset:0;background:linear-gradient(180deg,#8f72b7 0%,#7c5daa 45%,#6e4f9f 100%)}
.footer-inner{position:relative;padding-top:140px}
.footer-nav{display:flex;justify-content:center;gap:24px}
.footer-nav a{color:var(--white);text-decoration:none;font-size:22px}
.social{display:flex;justify-content:center;gap:18px;margin-top:26px}
.social span{width:46px;height:46px;border-radius:50%;background:var(--white)}
.copyright{margin-top:28px;font-size:12px;opacity:.9}
</style>
</head>
<body>

<section class="hero">
  <div class="hero-photo" role="img" aria-label="Photo of a purple sunset sky over the sea with waves on the shore"></div>
  <div class="hero-inner">
    <header class="site-header">
      <div class="logo">LOGO NAME</div>
      <nav class="main-nav">
        <a href="#">Home</a><a href="#">About me</a><a href="#">Blog</a><a href="#">Resume</a>
      </nav>
    </header>
    <h1>Lorem ipsum dolor sit amet</h1>
    <p class="hero-lead">Lorem ipsum dolor sit amet, consectetur adipiscing elit, sed do eiusmod tempor incididunt ut labore et dolore magna aliqua.</p>
    <a class="btn btn-outline" href="#">Read more</a>
  </div>
</section>

<section class="about">
  <h2 class="section-title">About me</h2>
  <p>Lorem ipsum dolor sit amet, consectetur adipiscing elit, sed do eiusmod tempor incididunt ut labore et dolore magna aliqua. Ut enim ad minim veniam, quis nostrud exercitation ullamco laboris nisi ut aliquip ex ea commodo consequat. Duis aute irure dolor in reprehenderit in voluptate velit esse cillum dolore eu fugiat nulla pariatur. Lorem ipsum dolor sit amet, consectetur adipiscing elit, sed do eiusmod tempor incididunt ut labore et dolore magna aliqua. Ut enim ad minim veniam, quis nostrud exercitation ullamco.</p>
  <a class="btn btn-solid" href="#">Download my resume</a>
</section>

<section class="mail">
  <div class="mail-photo" role="img" aria-label="Soft faded photo of a person in a field, tinted lilac"></div>
  <div class="mail-inner">
    <h2>Mail list registration</h2>
    <p>Lorem ipsum dolor sit amet, consectetur adipiscing elit, sed do eiusmod tempor incididunt ut labore et dolore magna aliqua.</p>
    <div class="signup">
      <div class="signup-field">Your email</div>
      <div class="signup-btn">Register now</div>
    </div>
  </div>
</section>

<section class="courses">
  <h2 class="section-title">Courses</h2>
  <div class="course-grid">
    <div class="course">
      <div class="course-icon"><svg width="34" height="34" viewBox="0 0 24 24" fill="none" stroke="#fff" stroke-width="1.6"><path d="M9 18h6M10 21h4M12 3a6 6 0 0 0-4 10.5c.7.7 1 1.5 1 2.5h6c0-1 .3-1.8 1-2.5A6 6 0 0 0 12 3z"/></svg></div>
      <div><h3>Lorem ipsum dolorsusd lduumyyxit amet</h3><p>Lorem ipsum dolor sit ametcon sectetur adipiscing elit, sed todo eiusmod tempor incididunt ut labore et dolore magna uo.</p></div>
    </div>
    <div class="course">
      <div class="course-icon"><svg width="34" height="34" viewBox="0 0 24 24" fill="none" stroke="#fff" stroke-width="1.6"><path d="M14 4c3-1 6-1 6-1s0 3-1 6l-6 6-4-4 5-7zM9 11l-4 1-2 3 4 0M13 15l-1 4-3 2 0-4M6 18l-2 2"/></svg></div>
      <div><h3>Lorem ipsum dolorsusd lduumyyxit amet</h3><p>Lorem ipsum dolor sit ametcon sectetur adipiscing elit, sed todo eiusmod tempor incididunt ut labore et dolore magna uo.</p></div>
    </div>
    <div class="course">
      <div class="course-icon"><svg width="32" height="32" viewBox="0 0 24 24" fill="none" stroke="#fff" stroke-width="1.6"><rect x="5" y="3" width="14" height="18" rx="1"/><path d="M8 8h8M8 12h8M8 16h5"/></svg></div>
      <div><h3>Lorem ipsum dolorsusd lduumyyxit amet</h3><p>Lorem ipsum dolor sit ametcon sectetur adipiscing elit, sed todo eiusmod tempor incididunt ut labore et dolore magna uo.</p></div>
    </div>
    <div class="course">
      <div class="course-icon"><svg width="34" height="34" viewBox="0 0 24 24" fill="none" stroke="#fff" stroke-width="1.6"><circle cx="12" cy="12" r="9"/><circle cx="12" cy="12" r="5"/><circle cx="12" cy="12" r="1.5"/></svg></div>
      <div><h3>Lorem ipsum dolorsusd lduumyyxit amet</h3><p>Lorem ipsum dolor sit ametcon sectetur adipiscing elit, sed todo eiusmod tempor incididunt ut labore et dolore magna uo.</p></div>
    </div>
  </div>
  <a class="btn btn-solid" href="#">Download my resume</a>
</section>

<section class="blog">
  <div class="blog-photo" role="img" aria-label="Faded lilac photo of a person in a meadow"></div>
  <div class="blog-inner">
    <h2 class="section-title">Blog</h2>
    <div class="blog-grid">
      <div class="blog-col">
        <article class="post"><h3>Lorem Ipsum is dummy typesetting industry.</h3><p>Sed ut perspiciatis unde omnis iste natus error sit voluptatem accusantium doloremque laudantium, totam rem aperiam, eaque ipsa quae ab illo inventore veritatis et quasi.</p><div class="post-date"><svg width="14" height="14" viewBox="0 0 24 24" fill="none" stroke="#6B429C" stroke-width="2"><rect x="3" y="5" width="18" height="16" rx="1"/><path d="M3 10h18M8 3v4M16 3v4"/></svg>21-12-2021</div></article>
        <article class="post"><h3>Lorem Ipsum is dummy typesetting fsxsf at perspi iatis unde omnis iste natu serror sit voluptatemt</h3><p>Sed ut perspiciatis unde omnis iste natus error sit voluptatem accusantium doloremque laudantium, totam rem aperiam, eaque ipsa quae ab illo inventore veritatis et quasi architecto beatae vitae dicta sunt explicabo.</p><div class="post-date"><svg width="14" height="14" viewBox="0 0 24 24" fill="none" stroke="#6B429C" stroke-width="2"><rect x="3" y="5" width="18" height="16" rx="1"/><path d="M3 10h18M8 3v4M16 3v4"/></svg>21-12-2021</div></article>
        <article class="post"><h3>Lorem Ipsum is dummy typesetting industry.</h3><p>Sed ut perspiciatis unde omnis iste natus error sit voluptatem accusantium doloremque laudantium, totam rem aperiam, eaque ipsa quae ab illo inventore veritatis et quasi.</p><div class="post-date"><svg width="14" height="14" viewBox="0 0 24 24" fill="none" stroke="#6B429C" stroke-width="2"><rect x="3" y="5" width="18" height="16" rx="1"/><path d="M3 10h18M8 3v4M16 3v4"/></svg>21-12-2021</div></article>
      </div>
      <div class="blog-col">
        <article class="post"><h3>Lorem Ipsum is dummy typesetting industry.</h3><p>Sed ut perspiciatis unde omnis iste natus error sit voluptatem accusantium doloremque laudantium, totam rem aperiam, eaque ipsa quae.</p><div class="post-date"><svg width="14" height="14" viewBox="0 0 24 24" fill="none" stroke="#6B429C" stroke-width="2"><rect x="3" y="5" width="18" height="16" rx="1"/><path d="M3 10h18M8 3v4M16 3v4"/></svg>21-12-2021</div></article>
        <article class="post"><h3>Lorem Ipsum is dummy typesetting industry.</h3><p>Sed ut perspiciatis unde omnis iste natus error sit voluptatem accusantium doloremque laudantium, totam rem aperiam, eaque ipsa quae.</p><div class="post-date"><svg width="14" height="14" viewBox="0 0 24 24" fill="none" stroke="#6B429C" stroke-width="2"><rect x="3" y="5" width="18" height="16" rx="1"/><path d="M3 10h18M8 3v4M16 3v4"/></svg>21-12-2021</div></article>
        <article class="post"><h3>Lorem Ipsum is dummy typesetting industry.</h3><p>Sed ut perspiciatis unde omnis iste natus error sit voluptatem accusantium doloremque laudantium, totam rem aperiam, eaque ipsa quae.</p><div class="post-date"><svg width="14" height="14" viewBox="0 0 24 24" fill="none" stroke="#6B429C" stroke-width="2"><rect x="3" y="5" width="18" height="16" rx="1"/><path d="M3 10h18M8 3v4M16 3v4"/></svg>21-12-2021</div></article>
        <article class="post"><h3>Lorem Ipsum is dummy typesetting industry.</h3><p>Sed ut perspiciatis unde omnis iste natus error sit voluptatem accusantium doloremque laudantium, totam rem aperiam, eaque ipsa quae.</p><div class="post-date"><svg width="14" height="14" viewBox="0 0 24 24" fill="none" stroke="#6B429C" stroke-width="2"><rect x="3" y="5" width="18" height="16" rx="1"/><path d="M3 10h18M8 3v4M16 3v4"/></svg>21-12-2021</div></article>
      </div>
      <div class="blog-col">
        <article class="post"><h3>Lorem Ipsum is dummy typesetting fsxsf at perspi iatis unde omnis iste natu serror sit voluptatemt</h3><p>Sed ut perspiciatis unde omnis iste natus error sit voluptatem accusantium doloremque laudantium, totam rem aperiam, eaque ipsa quae ab illo inventore veritatis et quasi.</p><div class="post-date"><svg width="14" height="14" viewBox="0 0 24 24" fill="none" stroke="#6B429C" stroke-width="2"><rect x="3" y="5" width="18" height="16" rx="1"/><path d="M3 10h18M8 3v4M16 3v4"/></svg>21-12-2021</div></article>
        <article class="post"><h3>Lorem Ipsum is dummy typesetting industry.</h3><p>Sed ut perspiciatis unde omnis iste natus error sit voluptatem accusantium doloremque laudantium, totam rem aperiam, eaque ipsa quae.</p><div class="post-date"><svg width="14" height="14" viewBox="0 0 24 24" fill="none" stroke="#6B429C" stroke-width="2"><rect x="3" y="5" width="18" height="16" rx="1"/><path d="M3 10h18M8 3v4M16 3v4"/></svg>21-12-2021</div></article>
        <article class="post"><h3>Lorem Ipsum is dummy typesetting industry.</h3><p>Sed ut perspiciatis unde omnis iste natus error sit voluptatem accusantium doloremque laudantium, totam rem aperiam, eaque ipsa quae.</p><div class="post-date"><svg width="14" height="14" viewBox="0 0 24 24" fill="none" stroke="#6B429C" stroke-width="2"><rect x="3" y="5" width="18" height="16" rx="1"/><path d="M3 10h18M8 3v4M16 3v4"/></svg>21-12-2021</div></article>
      </div>
    </div>
    <nav class="pager">
      <span class="active">01</span><span>02</span><span>03</span><span>04</span>
      <span><svg width="12" height="12" viewBox="0 0 24 24" fill="none" stroke="#fff" stroke-width="3"><path d="M9 5l7 7-7 7"/></svg></span>
    </nav>
  </div>
</section>

<footer class="site-footer">
  <div class="footer-photo" role="img" aria-label="Purple tinted photo of a person with raised arms in a field"></div>
  <div class="footer-inner">
    <nav class="footer-nav">
      <a href="#">Home</a><a href="#">About me</a><a href="#">Courses</a><a href="#">Blog</a><a href="#">Resume</a>
    </nav>
    <div class="social"><span></span><span></span><span></span><span></span><span></span></div>
    <p class="copyright">Copyright © 2021 Company name. All rights reserved.</p>
  </div>
</footer>

</body>
</html>
```